Elegant and modern Wedding Photography brochure

My existing brochure (attached) needs a major facelift. This is one of the main selling tools - it gets emailed to my clients when they make an equiry on what packages i offer and it is printed out and walked through at our first meeting. This brochure is as critical as my website - it needs to sing!

I'm looking for an eye-catching design that says:
Elegant
Modern
Clean
Crisp
Not cutesy or lovey-dovey thanks - we are more sophisticated and professional than that.

Update images to some of the latest weddings I've shot also. Let me know files and resolution you need. I've enabled right-click to download images on my site for a limited time. Please note that I retain copyright and will pursue any breeches.

Http://www.carlathornbey.com/Melbourne-wedding-photography
Updates

Thanks for all of your designs! Will take a few days to decide.

Target Market(s)

Australian Women aged 24-44

Industry/Entity Type

Wedding

Font styles to use
Other font styles liked:
• Century Gothic

Requirements
Must have
• Easy to print - does not have to be 6 A4 pages like the existing brochure
Nice to have
• Some full page images - The photos are supposed to be the hero here :-)
Should not have
• Not cutesy or lovey-dovey thanks - we are more sophisticated and professional than that.

No black backgrounds, I prefer a white thanks

No images in organic shaped boxes (like the rectangles in the logo - no thanks).
Keep the lines straight and sharp

```html
<!DOCTYPE html>
<html lang="en">
<head>
<meta charset="utf-8">
<title>Carla's approach – Wedding Photography Brochure</title>
<link href="https://fonts.googleapis.com/css2?family=Didact+Gothic&family=Mulish:wght@400;700&display=swap" rel="stylesheet">
<style>
  :root {
    --desk: #2b2b2b;
    --paper: #ffffff;
    --sage: #cde0a8;
    --frame: #dcdcdc;
    --ink: #1f1f1f;
    --label: #d8d8d8;
    --photo-bride: linear-gradient(135deg, #6d6a3c 0%, #b7a88f 45%, #dfe6ec 70%, #8f8a6a 100%);
    --photo-party: linear-gradient(180deg, #8a8a8a 0%, #4a4a4a 55%, #1e1e1e 100%);
    --photo-couple-mono: linear-gradient(160deg, #9a9a9a 0%, #3a3a3a 60%, #d8d8d8 100%);
    --photo-couple-colour: linear-gradient(160deg, #6c6a3a 0%, #a79c67 45%, #2a2a2a 80%, #e8ecee 100%);
  }
  * { box-sizing: border-box; margin: 0; padding: 0; }
  html, body { width: 1200px; height: 857px; overflow: hidden; }
  body {
    position: relative;
    background: var(--desk);
    font-family: "Mulish", "Century Gothic", sans-serif;
    color: var(--ink);
  }
  .spread-label {
    position: absolute; top: 4px;
    font-family: "Didact Gothic", sans-serif;
    font-size: 13px; color: var(--label);
  }
  .spread-label--left { left: 22px; }
  .spread-label--right { right: 22px; }

  .page {
    position: absolute; top: 22px;
    width: 574px; height: 812px;
    background: var(--paper);
  }
  .page--left { left: 25px; }
  .page--right { left: 600px; width: 575px; }

  .page__frame {
    position: absolute; left: 29px; top: 35px;
    width: 516px; height: 744px;
    border: 1px solid var(--frame);
  }
  .page__frame::after {
    content: ""; position: absolute; inset: 3px;
    border: 1px solid var(--frame);
  }
  .page__number {
    position: absolute; left: 278px; top: 768px;
    width: 18px; height: 18px;
    background: #e6efd4;
    transform: rotate(45deg);
  }
  .page__number span {
    display: block; transform: rotate(-45deg);
    font-size: 6px; line-height: 18px; text-align: center; color: #555;
  }

  .page__title {
    position: absolute; left: 61px; top: 74px;
    font-family: "Didact Gothic", "Century Gothic", sans-serif;
    font-weight: 400; font-size: 25px; line-height: 1; letter-spacing: .2px;
  }
  .page__subtitle {
    position: absolute; left: 61px; top: 106px;
    font-family: "Didact Gothic", "Century Gothic", sans-serif;
    font-weight: 400; font-size: 17px; line-height: 1;
  }

  .photo { position: absolute; }
  .photo--bride { left: 62px; top: 140px; width: 451px; height: 276px; background: var(--photo-bride); }
  .photo--party { left: 62px; top: 242px; width: 451px; height: 326px; background: var(--photo-party); }
  .photo--couple-mono { left: 62px; top: 578px; width: 182px; height: 169px; background: var(--photo-couple-mono); }
  .photo--couple-colour { left: 253px; top: 578px; width: 260px; height: 169px; background: var(--photo-couple-colour); }

  .section { position: absolute; left: 62px; width: 451px; }
  .section__heading {
    height: 17px; background: var(--sage);
    padding-left: 9px;
    font-family: "Didact Gothic", "Century Gothic", sans-serif;
    font-weight: 700; font-size: 12px; line-height: 17px;
    -webkit-text-stroke: .3px var(--ink);
  }
  .section__text {
    margin-top: 6px;
    font-size: 7.4px; line-height: 13.4px; text-align: justify;
  }
  .section__text + .section__text { margin-top: 7px; }

  .testimonials {
    position: absolute; left: 62px; top: 119px;
    width: 451px; height: 114px;
    background: var(--sage);
    display: flex; padding: 14px 18px 0;
  }
  .testimonial { font-size: 7.2px; line-height: 15.2px; }
  .testimonial--first { width: 211px; padding-right: 14px; text-align: justify; }
  .testimonial--second {
    width: 208px; padding-left: 14px;
    border-left: 1px solid #ffffff;
    height: 102px;
  }
  .testimonial__author { display: block; text-align: right; font-weight: 700; }
</style>
</head>
<body>
  <span class="spread-label spread-label--left">Pg-1</span>
  <span class="spread-label spread-label--right">Pg-2</span>

  <section class="page page--left">
    <div class="page__frame"></div>
    <h1 class="page__title">Carla’s approach…</h1>
    <p class="page__subtitle">Enjoy your special day!</p>
    <div class="photo photo--bride" role="img" aria-label="Portrait photograph of a smiling bride in a veil and lace gown, soft green background"></div>

    <div class="section" style="top:433px">
      <h2 class="section__heading">Style &amp; Approach</h2>
      <p class="section__text">Carla can observe and capture your wedding day in the background, quickly and quietly taking photojournalistic pictures rather than directing it if you prefer. Or she can confidently play the role of Art Director and instruct beautiful poses. Either way, what is most important is that her clients are relaxed and having a really great time on their wedding day!</p>
    </div>

    <div class="section" style="top:510px">
      <h2 class="section__heading">Formal Photography</h2>
      <p class="section__text">Many of Carla’s clients book her because of the easy-going approach she has. They can get on with having a great time on their day without worrying about formal photography. However, there are occasions when clients do want formal family pictures, and Carla is more than happy to accommodate their requests.</p>
      <p class="section__text">In order to keep the disruption on the day to a minimum, we recommend that Carla photographs no more than 6 groups, and a select number of the special couple.</p>
    </div>

    <div class="section" style="top:623px">
      <h2 class="section__heading">Image Presentation</h2>
      <p class="section__text">The most professional way of presenting clients with their photographs is in an elegantly designed photo book. Carla’s clients only pay one fixed price for the photography, regardless of how many images taken. There are no hard sell procedures to go through, and the completed book is prepared within 2-6 weeks after the wedding day.</p>
    </div>

    <div class="section" style="top:700px">
      <h2 class="section__heading">Time of Year</h2>
      <p class="section__text">Signature pictures can be taken on overcast days or winter months. Don’t worry if the sky is not perfectly blue. In the end, regardless of the weather – it’s the timeless mood of the day that Carla strives to capture.</p>
    </div>

    <div class="page__number"><span>1</span></div>
  </section>

  <section class="page page--right">
    <div class="page__frame"></div>
    <h1 class="page__title">What client’s are saying…</h1>

    <div class="testimonials">
      <blockquote class="testimonial testimonial--first">
        “Words can’t express my thanks Carla, I am absolutely in awe of my photos! You’ve captured my wedding day perfectly; couldn’t ask for anything more.”
        <cite class="testimonial__author">- Tess, Seddon</cite>
      </blockquote>
      <blockquote class="testimonial testimonial--second">
        “Thanks so much for photographing our special day, you did an amazing job and made everyone feel so comfortable. The amount of comments we have had on the photos so far has been wonderful and we couldn’t be happier!”
        <cite class="testimonial__author">- Naomi, Kensington</cite>
      </blockquote>
    </div>

    <div class="photo photo--party" role="img" aria-label="Black and white photograph of four groomsmen in suits with arms crossed before willow trees"></div>
    <div class="photo photo--couple-mono" role="img" aria-label="Black and white photograph of the bride and groom smiling together"></div>
    <div class="photo photo--couple-colour" role="img" aria-label="Colour photograph of the bride and groom standing beneath willow branches"></div>

    <div class="page__number"><span>2</span></div>
  </section>
</body>
</html>
```